ORBIT Freight Lane Inc is a shipping company focusing on small parcel ecommerce shipments. Parcels shipments like you would receive from Marketvale or Tradowen. We have amazing shipping rates for both domestic and international shipping. We will offer a full service solution with tracking of the parcel from beginning to end customer. We will employ state of the art technology in our shipping solution and also provide an easy to use interface that integrates with Cartlofter and the other top shipping platforms.

Target Market(s)

ecommerce shipping companies, marketvale sellers, small businesses, 3PL's

Coding

Coded - Design and coding required

Number of Pages Required

3 page

Requirements
Must have
• A login page which takes you to our dashboard interface
Package tracking on UI page
Nice to have
• A technology look and feel. The UX of the site should make the viewer feel that they are using the best most technologically advanced shipping solution on the market

We will also be tying this service as a value add to our sister company www.zelnor-example.com They should not look the same as they are separate companies, but would be nice if they had a similar flare
Should not have
• Warehouse 3PL feel with people delivering boxes. We do not deliver and are not a 3PL, we are a technological platform for shipping, specializing in international parcel rates.

```html
<!DOCTYPE html>
<html lang="en">
<head>
<meta charset="utf-8">
<title>ORBIT Freight Lane</title>
<link href="https://fonts.googleapis.com/css2?family=Poppins:ital,wght@0,400;0,500;0,600;0,700;1,400&family=Open+Sans:ital,wght@0,400;0,600;0,700;1,400&display=swap" rel="stylesheet">
<style>
:root{
  --purple:#4b3b8f;
  --purple-dark:#2a2160;
  --navy:#141a3a;
  --cyan:#3fa9f5;
  --orange:#f7941d;
  --ink:#222;
  --muted:#8a8a8a;
  --white:#fff;
}
*{box-sizing:border-box;margin:0;padding:0}
html,body{width:1200px;height:4435px;overflow:hidden}
body{position:relative;font-family:"Open Sans",sans-serif;color:var(--ink);background:var(--white)}
.abs{position:absolute}
.heading{font-family:"Poppins",sans-serif}

/* header */
.brand-block{left:0;top:0;width:370px;height:120px;background:var(--purple);display:flex;align-items:center;justify-content:center}
.brand{font-family:"Poppins",sans-serif;font-weight:700;font-size:23px;color:var(--white)}
.brand .accent{color:var(--orange)}
.call{left:522px;top:28px;display:flex;align-items:center;gap:10px;font-size:14px;color:#555}
.call b{font-family:"Poppins",sans-serif;font-size:20px;color:var(--ink);font-weight:600}
.call-icon{width:36px;height:36px;border-radius:50%;background:var(--orange);display:flex;align-items:center;justify-content:center}
.quote-btn{left:874px;top:16px;width:214px;height:52px;border-radius:26px;background:var(--orange);color:var(--white);font-family:"Poppins",sans-serif;font-weight:600;font-size:14px;display:flex;align-items:center;justify-content:center}
.nav{left:487px;top:85px;display:flex;gap:36px;font-size:14px;color:#333}
.nav .active,.nav .login{color:var(--orange)}

/* hero */
.hero-photo{left:0;top:120px;width:1200px;height:525px;background:
  radial-gradient(circle at 78% 45%,rgba(63,169,245,.45) 0,rgba(63,169,245,0) 38%),
  radial-gradient(circle at 62% 70%,rgba(247,148,29,.35) 0,rgba(247,148,29,0) 30%),
  linear-gradient(100deg,var(--navy) 0%,#1f2656 40%,#2d3a80 70%,#16204a 100%)}
.hero-cut{left:0;top:560px}
.hero-title{left:88px;top:268px;font-size:41px;font-weight:700;color:var(--white)}
.hero-text{left:88px;top:327px;width:440px;font-size:13px;line-height:25px;font-weight:600;color:var(--white)}
.hero-btn{left:88px;top:397px;width:150px;height:50px;border-radius:25px;background:var(--orange);color:var(--white);font-family:"Poppins",sans-serif;font-weight:600;font-size:14px;display:flex;align-items:center;justify-content:center}
.feature{top:645px;width:275px;height:171px;color:var(--white);text-align:center;padding-top:18px}
.feature.purple{background:var(--purple)}
.feature.orange{background:var(--orange)}
.feature-icon{width:46px;height:46px;margin:0 auto 12px;display:flex;align-items:center;justify-content:center}
.feature h4{font-size:13px;font-weight:400;margin-bottom:10px}
.feature p{font-size:13px;line-height:22px;padding:0 28px}

/* about */
.about-title{left:110px;top:908px;font-size:35px;font-weight:600}
.about-title span{color:var(--orange)}
.about-text{left:110px;top:966px;width:462px;font-size:13px;line-height:25.8px;color:#777}
.learn-btn{left:110px;top:1237px;width:176px;height:49px;border-radius:25px;background:var(--orange);color:var(--white);font-family:"Poppins",sans-serif;font-weight:600;font-size:13px;display:flex;align-items:center;justify-content:center}
.video{left:616px;top:921px;width:472px;height:365px;border-radius:50px 60px 0 60px;background:radial-gradient(circle at 50% 50%,#3fa9f5 0,#2c5fb0 24%,#2a2f78 48%,#1a1d45 80%,#120f2e 100%)}
.play{left:820px;top:1068px;width:64px;height:64px;border-radius:50%;background:var(--white);display:flex;align-items:center;justify-content:center}

/* services */
.services-band{left:0;top:1386px;width:1200px;height:453px;background:var(--orange)}
.services-kicker{left:0;top:1423px;width:1200px;text-align:center;font-size:14px;letter-spacing:2px;color:rgba(255,255,255,.25);font-weight:600}
.services-title{left:0;top:1448px;width:1200px;text-align:center;font-size:35px;font-weight:600;color:var(--white)}
.service{top:1541px;width:321px;height:370px;background:var(--white);box-shadow:0 4px 18px rgba(0,0,0,.1);text-align:center;padding-top:42px}
.service-frame{left:429px;top:1532px;width:337px;height:388px;border:8px solid var(--purple);border-left-color:transparent;border-bottom-color:transparent}
.service-frame2{left:429px;top:1532px;width:337px;height:388px;border:8px solid transparent;border-left-color:var(--purple);border-bottom-color:var(--purple);clip-path:polygon(0 50%,50% 50%,50% 100%,0 100%)}
.service-art{width:94px;height:84px;margin:0 auto 22px;border-radius:10px;background:linear-gradient(135deg,#3fa9f5,#4b3b8f 60%,#f7941d)}
.service h3{font-size:18px;font-weight:600;color:var(--purple);margin-bottom:16px}
.service p{font-size:13px;line-height:26px;color:#888;padding:0 22px}
.arrow-btn{width:60px;height:52px;border-radius:8px;margin:38px auto 0;display:flex;align-items:center;justify-content:center}
.arrow-btn.orange{background:var(--orange)}
.arrow-btn.purple{background:var(--purple)}

/* how it works */
.how-title{left:0;top:2005px;width:1200px;text-align:center;font-size:33px;font-weight:600}
.tile{width:474px;height:255px;display:flex;align-items:center;justify-content:center}
.tile span{font-family:"Poppins",sans-serif;font-size:24px;font-weight:600;color:var(--white)}
.tile.a{background:linear-gradient(135deg,#1c2452,#2f4d9a 60%,#3fa9f5)}
.tile.b{background:linear-gradient(135deg,#2a2160,#4b3b8f 55%,#6a5bb5)}
.tile.c{background:linear-gradient(135deg,#141a3a,#2c3c7a 55%,#4b3b8f)}
.tile.d{background:linear-gradient(135deg,#1a2a5a,#245a9a 55%,#1c2452)}

/* news */
.news-band{left:0;top:2717px;width:1200px;height:830px;background:var(--purple)}
.news-kicker{left:0;top:2772px;width:1200px;text-align:center;font-size:20px;letter-spacing:5px;color:var(--white)}
.news-title{left:0;top:2803px;width:1200px;text-align:center;font-size:33px;font-weight:600;color:var(--white)}
.news-card{background:var(--white)}
.news-img{flex:none;background:linear-gradient(135deg,#1c2452,#3fa9f5 55%,#dfe8f5)}
.news-img.b{background:linear-gradient(135deg,#2a2160,#4b3b8f 45%,#f7b45a)}
.news-img.c{background:linear-gradient(135deg,#141a3a,#2f4d9a 45%,#8fc8f5)}
.news-date{font-size:12px;color:#999;display:flex;align-items:center;gap:4px}
.news-date i{width:10px;height:10px;background:var(--orange);display:inline-block;border-radius:2px}
.news-h{font-family:"Poppins",sans-serif;font-size:20px;font-weight:500;line-height:26px;color:var(--ink)}
.news-p{font-size:13px;line-height:27px;color:#999}
.read{font-size:13px;font-weight:700;color:var(--orange);display:flex;align-items:center;gap:4px}
.more-btn{left:498px;top:3451px;width:203px;height:45px;background:var(--orange);color:var(--white);border-radius:4px;font-family:"Poppins",sans-serif;font-size:12px;font-weight:600;display:flex;align-items:center;justify-content:center}

/* testimonials */
.client-title{left:0;top:3625px;width:1200px;text-align:center;font-size:33px;font-weight:600}
.review{top:3702px;width:314px;height:190px;background:var(--white);box-shadow:0 3px 16px rgba(0,0,0,.1);text-align:center;padding-top:26px}
.review h5{font-size:17px;font-weight:600;color:var(--orange);margin-bottom:10px}
.review p{font-size:13px;font-style:italic;line-height:26px;color:#888;padding:0 30px}
.avatar{top:3847px;width:96px;height:96px;border-radius:50%;background:linear-gradient(160deg,#c9c9cf,#8c8f99);border:3px solid var(--white)}
.avatar.blue{background:linear-gradient(160deg,#4a8ad8,#2f5fa8)}
.chev{top:3796px;font-size:20px;color:#666}

/* footer */
.footer{left:0;top:4038px;width:1200px;height:397px;background:var(--purple)}
.foot-brand{left:113px;top:4165px;font-family:"Poppins",sans-serif;font-weight:700;font-size:23px;color:var(--orange)}
.socials{left:140px;top:4222px;display:flex;gap:8px}
.socials i{width:32px;height:32px;border:2px solid var(--white);background:var(--orange);display:block}
.foot-h{top:4105px;font-size:15px;font-weight:700;font-family:"Poppins",sans-serif;color:var(--white)}
.foot-list{list-style:none;font-size:13px;line-height:28.6px;color:var(--white)}
.foot-list li::before{content:"»";margin-right:12px}
.contact{color:var(--white)}
.contact-item{font-size:13px;line-height:28px;display:flex;gap:10px}
.contact-item b{color:var(--orange);font-weight:400}
.input{left:826px;width:266px;height:40px;background:var(--white);color:#888;font-size:13px;padding:10px 12px}
.submit{left:826px;top:4260px;width:102px;height:40px;background:var(--orange);color:var(--white);font-weight:700;font-size:14px;display:flex;align-items:center;justify-content:center;font-family:"Poppins",sans-serif}
.foot-line{left:112px;top:4360px;width:976px;height:1px;background:rgba(255,255,255,.25)}
.copy{left:0;top:4382px;width:1200px;text-align:center;font-size:13px;color:var(--white)}
</style>
</head>
<body>

<header>
  <div class="abs brand-block"><span class="brand">ORBIT Freight <span class="accent">Lane</span></span></div>
  <div class="abs call">
    <span class="call-icon"><svg width="18" height="18" viewBox="0 0 24 24"><path fill="#fff" d="M6.6 10.8a15 15 0 0 0 6.6 6.6l2.2-2.2c.3-.3.7-.4 1-.2 1.1.4 2.3.6 3.6.6.6 0 1 .4 1 1V20c0 .6-.4 1-1 1A17 17 0 0 1 3 4c0-.6.4-1 1-1h3.5c.6 0 1 .4 1 1 0 1.3.2 2.5.6 3.6.1.3 0 .7-.2 1z"/></svg></span>
    Call us Today : <b>+1 555 014 2290</b>
  </div>
  <div class="abs quote-btn">REQUEST A QUOTE</div>
  <nav class="abs nav">
    <span class="active">Home</span><span>About us</span><span>Services</span><span>Why us</span><span>Blog</span><span>Contact us</span><span>|</span><span class="login">Login</span>
  </nav>
</header>

<section class="hero">
  <div class="abs hero-photo" role="img" aria-label="Live parcel tracking dashboard over a glowing world route network"></div>
  <svg class="abs hero-cut" width="360" height="260" viewBox="0 0 360 260"><polygon points="0,0 360,190 360,260 0,260" fill="#fff"/></svg>
  <h1 class="abs hero-title heading">ORBIT FREIGHT LANE</h1>
  <p class="abs hero-text">Lorem ipsum dolor sit amet, consectetur adipiscing elit, sed do eiusmod tempor incididunt ut dolore magna aliqua.</p>
  <div class="abs hero-btn">GET STARTED</div>
  <div class="abs feature purple" style="left:358px"><div class="feature-icon"><svg width="40" height="40" viewBox="0 0 40 40" fill="none" stroke="#fff" stroke-width="2"><rect x="8" y="6" width="24" height="30" rx="2"/><path d="M13 14h14M13 20h14M13 26h9"/></svg></div><h4>EXPERIENCE</h4><p>Lorem ipsum dolor sit amet, conse ctetur adipiscing elitlabore</p></div>
  <div class="abs feature orange" style="left:642px"><div class="feature-icon"><svg width="40" height="40" viewBox="0 0 40 40" fill="none" stroke="#fff" stroke-width="2"><path d="M8 20l8 8 16-16"/></svg></div><h4>TRUST</h4><p>Lorem ipsum dolor sit amet, conse ctetur adipiscing elitlabore</p></div>
  <div class="abs feature purple" style="left:926px"><div class="feature-icon"><svg width="40" height="40" viewBox="0 0 40 40" fill="none" stroke="#fff" stroke-width="2"><circle cx="20" cy="18" r="10"/><path d="M20 12v12M17 15h5a2 2 0 0 1 0 4h-4a2 2 0 0 0 0 4h5M8 34h24"/></svg></div><h4>SAVINGS</h4><p>Lorem ipsum dolor sit amet, conse ctetur adipiscing elitlabore</p></div>
</section>

<section class="about">
  <h2 class="abs about-title heading">About <span>ORBIT Freight Lane</span></h2>
  <p class="abs about-text">Lorem ipsum dolor sit amet, consectetur adipiscing elit, sed do eiusmod tempor incididunt ut labore et dolore magna aliqua. Ut enim ad minim veniam, quis nostrud exercitation ullamco laboris nisi ut aliquip ex ea commodo consequat. Duis aute irure dolor in reprehenderit in voluptate velit esse cillum dolore eu fugiat nulla pariatur. Lorem ipsum dolor sit amet, consectetur adipiscing elit, sed do eiusmod tempor incididunt ut labore et dolore magna aliqua. Ut enim ad minim veniam, quis nostrud exercitation ullamco laboris nisi ut aliquip ex ea commodo consequat. Duis aute irure dolor in reprehenderit in voluptate velit esse cillum dolore eu fugiat nulla pariatur.</p>
  <div class="abs learn-btn">LEARN MORE</div>
  <div class="abs video" role="img" aria-label="Digital globe with international parcel routes and rate data"></div>
  <div class="abs play"><svg width="22" height="24" viewBox="0 0 22 24"><polygon points="3,2 20,12 3,22" fill="#4b3b8f"/></svg></div>
</section>

<section class="services">
  <div class="abs services-band"></div>
  <div class="abs services-kicker heading">WHAT WE DO</div>
  <h2 class="abs services-title heading">OUR SERVICES</h2>
  <div class="abs service-frame"></div>
  <div class="abs service-frame2"></div>
  <div class="abs service" style="left:72px"><div class="service-art" role="img" aria-label="Shipping rate comparison illustration"></div><h3>Lorem ipsum dolor</h3><p>Our expertise and experience covers many ore types and minerals, including iron ore, rare earths, mineral sands</p><div class="arrow-btn orange"><svg width="22" height="22" viewBox="0 0 22 22"><circle cx="11" cy="11" r="9" fill="none" stroke="#fff" stroke-width="2"/><path d="M7 11h8M11 7l4 4-4 4" fill="none" stroke="#fff" stroke-width="2"/></svg></div></div>
  <div class="abs service" style="left:437px"><div class="service-art" role="img" aria-label="Label printing and weight calculation illustration"></div><h3>Lorem ipsum dolor</h3><p>Our expertise and experience covers many ore types and minerals, including iron ore, rare earths, mineral sands</p><div class="arrow-btn purple"><svg width="22" height="22" viewBox="0 0 22 22"><circle cx="11" cy="11" r="9" fill="none" stroke="#fff" stroke-width="2"/><path d="M7 11h8M11 7l4 4-4 4" fill="none" stroke="#fff" stroke-width="2"/></svg></div></div>
  <div class="abs service" style="left:804px"><div class="service-art" role="img" aria-label="Global tracking pin illustration"></div><h3>Lorem ipsum dolor</h3><p>Our expertise and experience covers many ore types and minerals, including iron ore, rare earths, mineral sands</p><div class="arrow-btn orange"><svg width="22" height="22" viewBox="0 0 22 22"><circle cx="11" cy="11" r="9" fill="none" stroke="#fff" stroke-width="2"/><path d="M7 11h8M11 7l4 4-4 4" fill="none" stroke="#fff" stroke-width="2"/></svg></div></div>
</section>

<section class="how">
  <h2 class="abs how-title heading">HOW ORBIT FREIGHT LANE WORK</h2>
  <div class="abs tile a" style="left:112px;top:2084px" role="img" aria-label="Seller connecting an online store to the shipping platform"><span>Lorem ipsum dolor</span></div>
  <div class="abs tile b" style="left:613px;top:2084px" role="img" aria-label="Comparing international parcel rates on screen"><span>Lorem ipsum dolor</span></div>
  <div class="abs tile c" style="left:112px;top:2366px" role="img" aria-label="Creating shipping labels in the dashboard"><span>Lorem ipsum dolor</span></div>
  <div class="abs tile d" style="left:613px;top:2366px" role="img" aria-label="Live end-to-end tracking map on a tablet"><span>Lorem ipsum dolor</span></div>
</section>

<section class="news">
  <div class="abs news-band"></div>
  <div class="abs news-kicker heading">LATEST</div>
  <h2 class="abs news-title heading">NEWS FROM ORBIT FREIGHT LANE</h2>

  <article class="abs news-card" style="left:98px;top:2872px;width:319px;height:541px">
    <div class="news-img" style="height:228px" role="img" aria-label="Shipping analytics dashboard on a laptop"></div>
    <div style="padding:22px 32px 0">
      <div class="news-date"><i></i>Aug,2020</div>
      <h3 class="news-h" style="margin-top:8px">Lorem ipsum dolor sitam et, consectetur adipiscg elit, sed do eiusmod</h3>
      <p class="news-p" style="margin-top:12px">Lorem ipsum dolor sit amet, conse cte tur adipi scing elit, sed do eiusmod tem por incididunt ut labore et dolore mag na aliqua. Ut enim ad Lo rem</p>
      <div class="read" style="margin-top:10px">READ MORE ›</div>
    </div>
  </article>

  <article class="abs news-card" style="left:434px;top:2870px;width:665px;height:264px;display:flex">
    <div class="news-img b" style="width:255px;height:264px" role="img" aria-label="Mobile app showing parcel tracking status"></div>
    <div style="padding:22px 32px 0;flex:1">
      <div class="news-date"><i></i>Aug,2020</div>
      <h3 class="news-h" style="margin-top:12px">Lorem ipsum dolor sitam<br>et, consectetur adipiscg elit</h3>
      <p class="news-p" style="margin-top:8px">Lorem ipsum dolor sit amet, consectetur adipi scing elit, sed do eiusmod tempor incididunt ut labore et dolore magna aliqua. Ut enim ad</p>
      <div class="read" style="margin-top:10px">READ MORE ›</div>
    </div>
  </article>

  <article class="abs news-card" style="left:434px;top:3151px;width:665px;height:262px;display:flex">
    <div class="news-img c" style="width:255px;height:262px" role="img" aria-label="World map with international shipping lanes"></div>
    <div style="padding:22px 32px 0;flex:1">
      <div class="news-date"><i></i>Aug,2020</div>
      <h3 class="news-h" style="margin-top:12px">Lorem ipsum dolor sitam<br>et, consectetur adipiscg elit</h3>
      <p class="news-p" style="margin-top:8px">1.&nbsp; Lorem ipsum dolor sit amet, consectetur adipi scing elit, sed do eiusmod tempor incididunt ut labore et dolore magna aliqua. Ut enim ad Lo</p>
      <div class="read" style="margin-top:10px">READ MORE ›</div>
    </div>
  </article>

  <div class="abs more-btn">VIEW MORE NEWS</div>
</section>

<section class="clients">
  <h2 class="abs client-title heading">WHAT OUR CLIENT SAYS</h2>
  <span class="abs chev" style="left:50px">‹</span>
  <span class="abs chev" style="left:1135px">›</span>
  <div class="abs review" style="left:110px"><h5>John Doe</h5><p>Lorem ipsum dolor sit amet, consectetur adipiscing elit, sed do eiusmod tempor incididunt ut labore et dolore</p></div>
  <div class="abs review" style="left:443px"><h5>John Doe</h5><p>Lorem ipsum dolor sit amet, consectetur adipiscing elit, sed do eiusmod tempor incididunt ut labore et dolore</p></div>
  <div class="abs review" style="left:775px"><h5>John Doe</h5><p>Lorem ipsum dolor sit amet, consectetur adipiscing elit, sed do eiusmod tempor incididunt ut labore et dolore</p></div>
  <div class="abs avatar" style="left:219px" role="img" aria-label="Client portrait"></div>
  <div class="abs avatar" style="left:552px" role="img" aria-label="Client portrait"></div>
  <div class="abs avatar blue" style="left:884px" role="img" aria-label="Client portrait"></div>
</section>

<footer>
  <div class="abs footer"></div>
  <div class="abs foot-brand">ORBIT Freight Lane</div>
  <div class="abs socials"><i></i><i></i><i></i><i></i></div>
  <h4 class="abs foot-h" style="left:399px">INFORMATION</h4>
  <ul class="abs foot-list" style="left:399px;top:4146px">
    <li>Home</li><li>About</li><li>Services</li><li>Team</li><li>Blog</li><li>Contact us</li>
  </ul>
  <h4 class="abs foot-h" style="left:579px">CONTACT US</h4>
  <div class="abs contact" style="left:579px;top:4146px">
    <div class="contact-item"><b>●</b><span>123, Lorem Ipsum<br>simply dummy</span></div>
    <div class="contact-item" style="margin-top:22px"><b>✆</b><span>+1 555 014 2290</span></div>
    <div class="contact-item" style="margin-top:28px"><b>✉</b><span>info@orbitfreight-example.com</span></div>
  </div>
  <h4 class="abs foot-h" style="left:824px">NEWSLETTER</h4>
  <div class="abs input" style="top:4155px">Your Name</div>
  <div class="abs input" style="top:4206px">Enter Your Email Address</div>
  <div class="abs submit">SUBMIT</div>
  <div class="abs foot-line"></div>
  <p class="abs copy">© Copyrights Company name 2020. All rights reserved</p>
</footer>

</body>
</html>
```